Webpages for Sammalkivi Software Consulting

Needed: Webpage design.
Details:
One page site with good looking fonts and simple modern design. Logo would also be nice.
Page is for Software consulting company called: "Sammalkivi Software Consulting". Sammalkivi is my surname.
Pages should tell viewer that the company is reliable and its employees are hard-core professionals.
Company currently has one employee, that's me. So what I do is what this company does. I am software consultant. Basicly that means that I do Java/JavaEE/Web programming as subcontractor.
Here is more detail information about me.
SPECIALTIES
- Enterprise J2EE Application Programming and Architectures,
- Web development and
- Agile development.
I have over a decade of experience on designing and creating Java based web-services and applications to multiple interfaces. I also have plenty of experience about software architectures, design patterns and integration into third party systems. I’ve got good knowledge about agile software development and testing processes and I am experienced ScrumMaster and software project leader.
Target Market(s)
IT Businesses, Coding companies... Anyone who is buying coding as service.
Industry/Entity Type
Software

```html
<!DOCTYPE html>
<html lang="en">
<head>
<meta charset="utf-8">
<title>Sammalkivi Software Consulting</title>
<link rel="stylesheet" href="https://fonts.googleapis.com/css2?family=Arimo:wght@400&family=Arvo&display=swap">
<style>
  :root {
    --page-bg: #ffffff;
    --body-text: #111418;
    --heading-text: #1c2530;
    --band-bg: #e0e0e0;
    --badge-tone: #8c8c8c;
    --badge-light: #b4b4b4;
    --footer-bg: #262626;
    --footer-text: #e6e6e6;
    --logo-text: #d9d9d9;
    --icon-top: #f4f4f4;
    --icon-bottom: #bdbdbd;
  }
  * { margin: 0; padding: 0; box-sizing: border-box; }
  html, body { width: 1200px; height: 884px; overflow: hidden; background: var(--page-bg); }
  body { position: relative; font-family: "Arimo", Arial, sans-serif; color: var(--body-text); }

  .content { position: absolute; left: 0; top: 0; width: 1200px; height: 318px; }
  .content p {
    position: absolute; left: 187px; width: 840px;
    font-size: 12px; line-height: 14px;
  }
  .intro-text { top: 11px; }
  .section-title {
    position: absolute; left: 187px; top: 98px;
    font-family: "Arvo", Georgia, serif; font-weight: 400;
    font-size: 19px; color: var(--heading-text);
  }
  .agile-text { top: 140px; }

  .partners {
    position: absolute; left: 0; top: 318px; width: 1200px; height: 182px;
    background: var(--band-bg);
    box-shadow: inset 0 4px 4px -2px rgba(0,0,0,0.25), inset 5px 0 5px -3px rgba(0,0,0,0.2);
  }
  .badge { position: absolute; background: var(--badge-tone); }
  .badge-wide { left: 177px; top: 71px; width: 122px; height: 36px; border-radius: 18px; background: var(--badge-light); }
  .badge-square { left: 395px; top: 53px; width: 72px; height: 72px; }
  .badge-mascot { left: 592px; top: 60px; width: 66px; height: 58px; border-radius: 29px; background: linear-gradient(#c8c8c8, #a6a6a6); }
  .badge-award { left: 794px; top: 53px; width: 48px; height: 48px; transform: rotate(45deg) scale(0.8); }
  .badge-award-base { left: 765px; top: 116px; width: 104px; height: 10px; background: var(--badge-light); }
  .badge-edge { left: 990px; top: 57px; width: 41px; height: 66px; background: linear-gradient(90deg, #cfcfcf, #6f6f6f); }

  .site-footer {
    position: absolute; left: 0; top: 500px; width: 1200px; height: 384px;
    background: var(--footer-bg); color: var(--footer-text); text-align: center;
  }
  .brand { position: absolute; left: 506px; top: 50px; display: flex; align-items: center; gap: 12px; }
  .brand-mark { width: 52px; height: 68px; background: var(--logo-text); }
  .brand-name {
    text-align: left; color: var(--logo-text); font-size: 22px; line-height: 22px; letter-spacing: 0.5px;
  }
  .brand-name span { display: block; font-size: 13px; line-height: 16px; letter-spacing: 0.3px; }
  .contact { position: absolute; top: 167px; width: 100%; font-size: 14px; line-height: 17px; }
  .social { position: absolute; top: 220px; left: 552px; display: flex; gap: 14px; }
  .social-icon {
    width: 29px; height: 29px; border-radius: 5px;
    background: linear-gradient(var(--icon-top), var(--icon-bottom));
  }
  .legal { position: absolute; top: 280px; width: 100%; font-size: 12px; line-height: 20px; }
  .legal a { color: var(--footer-text); text-decoration: underline; }
  .legal .sep { margin: 0 5px; }
</style>
</head>
<body>
  <main class="content">
    <p class="intro-text">Lorem ipsum dolor sit amet, consectetur adipiscing elit. Nullam adipiscing eros tellus. Fusce pulvinar sem ut risus varius tincidunt. Donec scelerisque suscipit felis, eget convallis mi porta a. Sed eget lobortis dolor. Donec cursus rhoncus rutrum. Nam tristique purus ac dui ultricies nec faucibus turpis aliquet. In risus diam, facilisis ut dictum eu, tristique sit amet ante.</p>
    <h2 class="section-title">Agile development</h2>
    <p class="agile-text">Lorem ipsum dolor sit amet, consectetur adipiscing elit. Nullam adipiscing eros tellus. Fusce pulvinar sem ut risus varius tincidunt. Donec scelerisque suscipit felis, eget convallis mi porta a. Sed eget lobortis dolor. Donec cursus rhoncus rutrum. Nam tristique purus ac dui ultricies nec faucibus turpis aliquet. In risus diam, facilisis ut dictum eu, tristique sit amet ante.</p>
  </main>

  <section class="partners" aria-label="Awards and partners">
    <div class="badge badge-wide"></div>
    <div class="badge badge-square"></div>
    <div class="badge badge-mascot" role="img" aria-label="Partner mascot illustration"></div>
    <div class="badge badge-award"></div>
    <div class="badge badge-award-base"></div>
    <div class="badge badge-edge"></div>
  </section>

  <footer class="site-footer">
    <div class="brand">
      <div class="brand-mark"></div>
      <div class="brand-name">SAMMALKIVI<span>SOFTWARE CONSULTING</span></div>
    </div>
    <div class="contact">
      Loft 4, 28 Mill Lane, Ashbridge, Kent, AB1 2CD<br>
      t: 100 200 30000 &nbsp; e: hello@sammalkivi.example
    </div>
    <div class="social" aria-label="Social links">
      <span class="social-icon"></span>
      <span class="social-icon"></span>
      <span class="social-icon"></span>
    </div>
    <div class="legal">
      &copy; Copyright 2011<br>
      <a href="#">Terms &amp; Conditions</a><span class="sep">|</span><a href="#">Privacy Policy</a>
    </div>
  </footer>
</body>
</html>
```